Spino-Tarla
business card/ stationary
Spino-Tarla - Health
Creative Brief
Professional
Dr. Martin Pettigrew
Chiropractic Physician, CHO
914 Halden Rd Marrow Cove, CA 92318
mpw@spino-tarla.example
www.spino-tarla.example
use small logo as bullet for back of business card info. line 1 Health - Happiness - Abundance then bullets
Health - Happiness - Abundance - Natural Chiropractic Care: family wellness, chronic pain relief, personal injury - Balanced Living Consultation: conscious lifestyle programs for stress management, nutrition, weight loss, physical and emotional balance - Quiet Current Stillness Practice: group and private instruction - Wellbeing Educational Seminars

```html
<!DOCTYPE html>
<html lang="en">
<head>
<meta charset="utf-8">
<title>Spino-Tarla Stationery</title>
<link rel="stylesheet" href="https://fonts.googleapis.com/css2?family=Open+Sans:wght@400;600&display=swap">
<style>
  :root {
    --bg: #e9e4dc;
    --paper: #ffffff;
    --brand-blue: #2b62a8;
    --accent-orange: #e07b2a;
    --leaf-green: #7fae4a;
    --ink: #555555;
    --rule: #b9b9b9;
    --shadow: rgba(0,0,0,0.18);
  }
  * { box-sizing: border-box; margin: 0; padding: 0; }
  html, body { width: 1200px; height: 562px; overflow: hidden; }
  body {
    background: var(--bg);
    font-family: "Open Sans", Arial, sans-serif;
    color: var(--ink);
    position: relative;
  }
  .sheet {
    position: absolute;
    background: var(--paper);
    box-shadow: 0 2px 6px var(--shadow);
    overflow: hidden;
  }
  .fax-cover { left: 14px; top: 29px; width: 376px; height: 523px; }
  .letterhead { left: 408px; top: 29px; width: 374px; height: 523px; }
  .card-front { left: 800px; top: 34px; width: 184px; height: 105px; }
  .card-back { left: 996px; top: 34px; width: 185px; height: 105px; }
  .envelope-front { left: 800px; top: 170px; width: 381px; height: 190px; }
  .envelope-back { left: 800px; top: 372px; width: 381px; height: 180px; }

  .brand { text-align: center; }
  .brand-name {
    font-family: "Open Sans", Arial, sans-serif;
    font-weight: 600;
    color: var(--brand-blue);
    line-height: 1.1;
  }
  .brand-tagline {
    font-weight: 400;
    color: var(--ink);
    line-height: 1.5;
  }
  .sheet-brand { position: absolute; top: 24px; left: 0; right: 0; }
  .sheet-brand .brand-name { font-size: 22px; }
  .sheet-brand .brand-tagline { font-size: 7px; }

  .sheet-footer {
    position: absolute; left: 20px; right: 20px; bottom: 12px;
    text-align: center; font-size: 5.5px; color: var(--ink);
    border-top: 1px solid var(--leaf-green);
    padding-top: 4px;
  }

  .fax-label {
    position: absolute; right: 26px; top: 82px;
    font-size: 9px; font-weight: 600; letter-spacing: 1px; color: #333;
  }
  .fax-fields {
    position: absolute; left: 24px; top: 96px;
    border-collapse: collapse; width: 328px;
    font-size: 6.5px;
  }
  .fax-fields td { border: 1px solid var(--rule); height: 21px; padding: 0 5px; }
  .fax-fields .field-name { width: 38px; }
  .fax-options {
    position: absolute; left: 24px; right: 24px; top: 190px;
    display: flex; justify-content: space-between; font-size: 6px;
  }
  .fax-options span::before {
    content: ""; display: inline-block; width: 6px; height: 6px;
    border: 1px solid #777; margin-right: 3px; vertical-align: -1px;
  }

  .card-front .brand { position: absolute; top: 14px; left: 0; right: 0; }
  .card-front .brand-name { font-size: 13px; }
  .card-front .brand-tagline { font-size: 4.5px; }
  .card-contact {
    position: absolute; left: 0; right: 0; top: 56px;
    text-align: center; font-size: 5px; line-height: 1.5;
  }
  .card-contact .person { color: var(--brand-blue); font-weight: 600; font-size: 5.5px; }
  .card-band { position: absolute; left: 0; right: 0; bottom: 0; height: 6px; background: var(--leaf-green); }

  .card-back { padding: 9px 10px; font-size: 4.5px; line-height: 1.45; }
  .card-back .pillars { text-align: center; color: var(--accent-orange); font-weight: 600; font-size: 5px; margin-bottom: 5px; }
  .card-back ul { list-style: none; }
  .card-back li { position: relative; padding-left: 7px; margin-bottom: 2.5px; }
  .card-back li::before {
    content: ""; position: absolute; left: 0; top: 1.6px;
    width: 3.5px; height: 3.5px; border-radius: 50%; background: var(--accent-orange);
  }

  .envelope-front .brand { position: absolute; left: 18px; top: 16px; text-align: left; }
  .envelope-front .brand-name { font-size: 16px; }
  .envelope-front .brand-tagline { font-size: 5px; }
  .envelope-return { position: absolute; left: 18px; top: 56px; font-size: 5px; }

  .envelope-back svg { position: absolute; left: 0; top: 0; }
  .envelope-back .brand { position: absolute; left: 0; right: 0; top: 38px; }
  .envelope-back .brand-name { font-size: 12px; }
  .envelope-back .brand-tagline { font-size: 4.5px; }
</style>
</head>
<body>

<section class="sheet fax-cover">
  <div class="brand sheet-brand">
    <div class="brand-name">Spino-Tarla</div>
    <div class="brand-tagline">Centre for Whole Balance</div>
  </div>
  <div class="fax-label">FAX</div>
  <table class="fax-fields">
    <tr><td class="field-name">To:</td><td></td><td class="field-name">From:</td><td></td></tr>
    <tr><td class="field-name">Fax:</td><td></td><td class="field-name">Pages:</td><td></td></tr>
    <tr><td class="field-name">Phone:</td><td></td><td class="field-name">Date:</td><td></td></tr>
    <tr><td class="field-name">Re:</td><td></td><td class="field-name">CC:</td><td></td></tr>
  </table>
  <div class="fax-options">
    <span>Urgent</span><span>For Review</span><span>Please Comment</span><span>Please Reply</span><span>Please Recycle</span>
  </div>
  <div class="sheet-footer">914 Halden Rd, Marrow Cove, CA 92318 &nbsp;|&nbsp; mpw@spino-tarla.example &nbsp;|&nbsp; www.spino-tarla.example</div>
</section>

<section class="sheet letterhead">
  <div class="brand sheet-brand">
    <div class="brand-name">Spino-Tarla</div>
    <div class="brand-tagline">Centre for Whole Balance</div>
  </div>
  <div class="sheet-footer">914 Halden Rd, Marrow Cove, CA 92318 &nbsp;|&nbsp; mpw@spino-tarla.example &nbsp;|&nbsp; www.spino-tarla.example</div>
</section>

<section class="sheet card-front">
  <div class="brand">
    <div class="brand-name">Spino-Tarla</div>
    <div class="brand-tagline">Centre for Whole Balance</div>
  </div>
  <div class="card-contact">
    <div class="person">Dr. Martin Pettigrew</div>
    <div>Chiropractic Physician, CHO</div>
    <div>914 Halden Rd Marrow Cove, CA 92318</div>
    <div>mpw@spino-tarla.example &nbsp; www.spino-tarla.example</div>
  </div>
  <div class="card-band"></div>
</section>

<section class="sheet card-back">
  <div class="pillars">Health - Happiness - Abundance</div>
  <ul>
    <li>Gentle Spinal Care: family visits, back and neck relief, injury recovery</li>
    <li>Balanced Living Consultation: daily routine plans for calmer days, better meals, steady energy and rest</li>
    <li>Quiet Current Stillness Practice: group and private instruction</li>
    <li>Community Wellbeing Talks</li>
  </ul>
</section>

<section class="sheet envelope-front">
  <div class="brand">
    <div class="brand-name">Spino-Tarla</div>
    <div class="brand-tagline">Centre for Whole Balance</div>
  </div>
  <div class="envelope-return">914 Halden Rd Marrow Cove, CA 92318</div>
</section>

<section class="sheet envelope-back">
  <svg width="381" height="180" viewBox="0 0 381 180" aria-hidden="true">
    <path d="M0 0 L190 88 L381 0" fill="none" stroke="#cfcfcf" stroke-width="1"/>
    <path d="M0 180 L150 70 M381 180 L231 70" fill="none" stroke="#e2e2e2" stroke-width="1"/>
  </svg>
  <div class="brand">
    <div class="brand-name">Spino-Tarla</div>
    <div class="brand-tagline">Centre for Whole Balance</div>
  </div>
</section>

</body>
</html>
```